Business Card Design

I need Business card designs with following on cards:

Dalton Mewse
Director

M: +61 491 268 304
D: +61 7 5590 1826
F: +61 7 5590 6071
E: dalton@torvelgroup.com.au

Torvel Group
Suite 4/58 North Calloway Road
Corvale Heads QLD 4299

Rex Halloran
Director

M: +61 438 952 107
D: +61 7 5590 1826
F: +61 7 5590 6071
E: rex@torvelgroup.com.au

Torvel Group
Corvale Heads QLD 4299

Torvel Group Logo has been attached to brief.

```html
<!DOCTYPE html>
<html lang="en">
<head>
<meta charset="utf-8">
<title>Torvel Group – Business Cards</title>
<link rel="stylesheet" href="https://fonts.googleapis.com/css2?family=Arimo:wght@400;700&family=Tinos&display=swap">
<style>
  :root {
    --page: #ffffff;
    --card: #050505;
    --ink-light: #f2f2f2;
    --ink-dark: #111111;
    --panel-orange: #e8612a;
    --panel-orange-deep: #d4461c;
    --glow-navy: #1a1f55;
    --glow-blue: #3b46c8;
    --glow-violet: #6a3aa8;
    --glow-red: #c8281c;
    --glow-amber: #e08a1c;
  }
  * { box-sizing: border-box; margin: 0; padding: 0; }
  html, body {
    width: 1200px; height: 960px; overflow: hidden;
    background: var(--page);
  }
  .sheet { position: relative; width: 1200px; height: 960px; }

  .card {
    position: absolute; width: 525px; height: 300px;
    background: var(--card);
    overflow: hidden;
    box-shadow: 0 6px 18px rgba(0,0,0,0.18);
  }
  .card--back { left: 337px; top: 120px; }
  .card--front-dalton { left: 50px; top: 500px; }
  .card--front-rex { left: 625px; top: 500px; }

  /* Back: company side */
  .back-strip {
    position: absolute; left: 0; top: 0; width: 58px; height: 300px;
    background: linear-gradient(180deg, var(--card) 15%, var(--glow-blue) 38%, var(--glow-red) 58%, var(--glow-amber) 72%, var(--card) 92%);
    opacity: 0.85;
  }
  .brand-name {
    position: absolute; left: 150px; top: 90px;
    font-family: "Arimo", sans-serif; font-weight: 700;
    font-size: 34px; letter-spacing: 1px;
    color: var(--ink-light); text-transform: uppercase;
  }
  .address {
    position: absolute; right: 30px; top: 160px;
    font-family: "Arimo", sans-serif; font-size: 11px;
    color: var(--ink-light); text-align: right; line-height: 36px;
  }

  /* Front: contact side */
  .front-photo {
    position: absolute; left: 190px; right: 0; top: 70px; bottom: 18px;
    background: linear-gradient(180deg, var(--glow-navy) 0%, var(--glow-blue) 35%, var(--glow-violet) 55%, var(--glow-red) 75%, var(--glow-amber) 100%);
    -webkit-mask-image: linear-gradient(90deg, transparent 0%, #000 35%);
    mask-image: linear-gradient(90deg, transparent 0%, #000 35%);
    opacity: 0.8;
  }
  .panel {
    position: absolute;
    background: linear-gradient(90deg, var(--panel-orange-deep), var(--panel-orange));
    font-family: "Tinos", serif; color: var(--ink-dark);
  }
  .panel--name {
    left: 22px; top: 14px; width: 225px; height: 56px;
    text-align: center; font-size: 20px; line-height: 22px; padding-top: 6px;
  }
  .panel--contact {
    left: 18px; top: 159px; width: 234px; height: 122px;
    font-size: 14px; line-height: 20px; padding: 12px 0 0 15px;
  }
  .contact-line span { display: inline-block; width: 20px; }
</style>
</head>
<body>
<main class="sheet">
  <section class="card card--back" aria-label="Card back">
    <div class="back-strip" role="img" aria-label="Strip of colourful bokeh light photograph"></div>
    <div class="brand-name">Torvel Group</div>
    <div class="address">
      <p>Suite 4/58 North Calloway Road</p>
      <p>Corvale Heads QLD 4299</p>
    </div>
  </section>

  <section class="card card--front-dalton" aria-label="Card front, Dalton Mewse">
    <div class="front-photo" role="img" aria-label="Bokeh light photograph in blue, violet, red and amber"></div>
    <div class="panel panel--name">
      <p>Dalton Mewse</p>
      <p>Director</p>
    </div>
    <div class="panel panel--contact">
      <p class="contact-line"><span>M:</span>61 491 268 304</p>
      <p class="contact-line"><span>D:</span>61 7 5590 1826</p>
      <p class="contact-line"><span>F:</span>61 7 5590 6071</p>
      <p class="contact-line"><span>E:</span>dalton@torvelgroup.com.au</p>
    </div>
  </section>

  <section class="card card--front-rex" aria-label="Card front, Rex Halloran">
    <div class="front-photo" role="img" aria-label="Bokeh light photograph in blue, violet, red and amber"></div>
    <div class="panel panel--name">
      <p>Rex Halloran</p>
      <p>Director</p>
    </div>
    <div class="panel panel--contact">
      <p class="contact-line"><span>M:</span>61 438 952 107</p>
      <p class="contact-line"><span>D:</span>61 7 5590 1826</p>
      <p class="contact-line"><span>F:</span>61 7 5590 6071</p>
      <p class="contact-line"><span>E:</span>rex@torvelgroup.com.au</p>
    </div>
  </section>
</main>
</body>
</html>
```